Business Card template designs

We need a lot of Business card designs.
Your designs will get exposure on our newly opened business-card printing website.
We are committed to quality of paper and packages we use, so they will come up very fancy.

Here is your advantage. We will put the profile of the graphic designer on our site so that you can showcase your designs to people around the world and in Japan.

A profile is not mandatory, although we encourage graphic designers to have a profile to get continuous work in the future.
We are looking forward to having many good designs.

The right of the use of design will be owned by us.
The design may be used to the products other than
business cards.

Target Market(s)

designer,photographer,creator,artist

Industry/Entity Type

Printing

Contact Information for Business Card

The back design is important.
Please check the reference file.

Requirements
Must have
• Please include the following, required information on your business card designs.
• Name: Haruna Okabe
• Title: Designer
• Web: https://www.ketori.co.jp/kt/
• Address: 4-17 Kamiharuta-Cho Meguro-ku, Tokyo
• Email: info@kketori.com
• Phone: 03 4816 3907
• Mobile: 070 2143 6658
• * For Japanese sites, we will convert the text portion to Japanese characters.
• * In case of 28mmx70mm only include Name,Enail,Phone and SNS account(https://www.facebook.com/kketori.com)
• 1. colorful
• 2. simple
• 3. natural
• 4. modern
• 5. cool
• 6. sporty
• Please make variations of the same image with 3-6
• different colors / patterns for one design so that
• customers can compare and choose.
• If you want to use a same picture, please make make
• copies and paste on each different types of design.
Nice to have
• You may also use, the following non-required information.
• Company Name: Ketori, Inc.
• Fax: 03-4173-9620
• Open space for company logo

```html
<!DOCTYPE html>
<html lang="en">
<head>
<meta charset="utf-8">
<title>Business Card — Front and Back</title>
<link href="https://fonts.googleapis.com/css2?family=Josefin+Sans:wght@300&family=Open+Sans:wght@400&display=swap" rel="stylesheet">
<style>
  :root {
    --bg: #e9e5df;
    --orange: #dd6310;
    --orange-bright: #f27214;
    --ink: #141414;
    --text: #2b2b2b;
    --paper: #ffffff;
  }
  * { box-sizing: border-box; margin: 0; padding: 0; }
  html, body { width: 1200px; height: 800px; overflow: hidden; background: var(--bg); }
  .stage { position: relative; width: 1200px; height: 800px; }
  .card {
    position: absolute; top: 170px; width: 460px; height: 460px;
    box-shadow: 0 10px 28px rgba(0,0,0,0.18);
  }
  .card--front { left: 110px; background: var(--orange); }
  .card--back { left: 630px; background: var(--paper); }

  .brand {
    position: absolute; left: 92px; top: 205px;
    display: flex; align-items: center; gap: 16px;
  }
  .brand__mark { width: 46px; height: 46px; border-radius: 50%; background: var(--ink); }
  .brand__name {
    font-family: "Josefin Sans", sans-serif; font-weight: 300;
    font-size: 27px; letter-spacing: 7px; color: var(--ink); line-height: 1;
  }

  .back__mark {
    position: absolute; left: 200px; top: 62px;
    width: 58px; height: 58px; border-radius: 50%; background: var(--orange-bright);
  }
  .contact {
    position: absolute; left: 58px; top: 262px;
    font-family: "Open Sans", sans-serif; color: var(--text);
  }
  .contact__name { font-size: 27px; line-height: 1.1; }
  .contact__title { font-size: 17px; color: var(--orange-bright); margin: 2px 0 12px; }
  .contact__list { list-style: none; }
  .contact__item {
    display: flex; align-items: center; gap: 12px;
    font-size: 15px; line-height: 26px;
  }
  .contact__icon { width: 14px; height: 14px; flex: none; fill: var(--orange-bright); }
</style>
</head>
<body>
<main class="stage">
  <section class="card card--front" aria-label="Card front">
    <div class="brand">
      <span class="brand__mark" aria-hidden="true"></span>
      <span class="brand__name">COMPANY NAME</span>
    </div>
  </section>

  <section class="card card--back" aria-label="Card back">
    <span class="back__mark" aria-hidden="true"></span>
    <div class="contact">
      <p class="contact__name">Haruna Okabe</p>
      <p class="contact__title">Designer</p>
      <ul class="contact__list">
        <li class="contact__item">
          <svg class="contact__icon" viewBox="0 0 14 14" aria-hidden="true"><path d="M1 4c0-2 1-3 2-3h8c1 0 2 1 2 3v1H9V3.5H5V5H1z"/><rect x="2" y="6" width="10" height="7" rx="1"/></svg>
          03 4816 3907
        </li>
        <li class="contact__item">
          <svg class="contact__icon" viewBox="0 0 14 14" aria-hidden="true"><path d="M3 1h8v12H3zM4.3 2.3v9.4h5.4V2.3z"/></svg>
          070 2143 6658
        </li>
        <li class="contact__item">
          <svg class="contact__icon" viewBox="0 0 14 14" aria-hidden="true"><path d="M1 3h12v8H1zM1.5 3.5 7 8l5.5-4.5v1L7 9 1.5 4.5z"/></svg>
          info@kketori.com
        </li>
        <li class="contact__item">
          <svg class="contact__icon" viewBox="0 0 14 14" aria-hidden="true"><path d="M7 1a6 6 0 1 0 0 12A6 6 0 0 0 7 1zm0 1.3a4.7 4.7 0 1 1 0 9.4 4.7 4.7 0 0 1 0-9.4zM2.5 6.4h9v1.2h-9zM6.4 2.5h1.2v9H6.4z"/></svg>
          www.ketori.co.jp/kt/
        </li>
        <li class="contact__item">
          <svg class="contact__icon" viewBox="0 0 14 14" aria-hidden="true"><path d="M7 1a4.5 4.5 0 0 0-4.5 4.5C2.5 9 7 13 7 13s4.5-4 4.5-7.5A4.5 4.5 0 0 0 7 1zm0 2.6a1.9 1.9 0 1 1 0 3.8 1.9 1.9 0 0 1 0-3.8z"/></svg>
          4-17 Kamiharuta-Cho Meguro-ku, Tokyo
        </li>
      </ul>
    </div>
  </section>
</main>
</body>
</html>
```